Custom Framing Shop Tallpine Framing Studio

I want an eye catching graphic that will be used a s business sign on a busy road. The sign MUST communicate the type of business it is clearly to vehicles traveling at 40 mph. This is a custom picture framing business and the sign will be hanging and be approximately 32" X 48". The business name is Tallpine Framing Studio; Custom framing: by appointment and should include a whole or partial image of a picture frame as a visual que. I've included inspiration idea's, color pallets and styles that I like and a current business card for inspiration. I like the crimson font style shadowing and background colors of the attached Olans pizzeria sign. I'd prefer crimson letters. Custom Framing is the message to communicate, followed by phone number and business name. I like the idea of a shield shape with a banner since it would more eye catching, Once again the Tallpine image and name is less important than communicating what the business does. I like Crimson, grey, gold, black but am open to new ideas . I like the idea of a shield with a banner more than a rectangle, but am open to idea's

Target Market(s)

My target market is local homeowners ($700k+) who want a relationship with their framer and are willing to pay for a customized experience compared to a craft store experience. I have more female clients then men.

Industry/Entity Type

Picture Framing Art

Other font styles liked:
• Look at the attached image of a custom pizzeria sign, its kid of a custom car pinstripe font style. Script and decorative may be difficult to read while driving by but add to the elegance.

Colors

Designer to choose colors to be used in the design.

Requirements
Must have
• Clearly communicate what the business does "Custom framing" preferably with a picture frame and words
Nice to have
• incorporate a Tallpine into the graphic
Should not have
• A Tallpine image doesn't communicate what the business does to a vehicle traveling at 40 mph by the sign

```html
<!DOCTYPE html>
<html lang="en">
<head>
<meta charset="utf-8">
<title>Tallpine Framing Studio – Hanging Sign</title>
<link rel="stylesheet" href="https://fonts.googleapis.com/css2?family=Rye&family=Alfa+Slab+One&family=Libre+Caslon+Text:wght@400;700&family=Oswald:wght@500&display=swap">
<style>
  :root {
    --backdrop: #e9e6e0;
    --sign-black: #141414;
    --gold: #d9b44a;
    --gold-light: #ecd37f;
    --gold-deep: #a9812a;
    --crimson: #a3161c;
    --crimson-dark: #7e1417;
    --cream: #f3ecdc;
    --ink: #2a1a0c;
  }
  html, body {
    margin: 0;
    width: 1200px;
    height: 900px;
    overflow: hidden;
    background: var(--backdrop);
  }
  .sign {
    position: absolute;
    left: 305px;
    top: 10px;
    width: 590px;
    height: 880px;
  }
  .sign-name {
    font-family: "Rye", serif;
    fill: var(--crimson);
  }
  .sign-subtitle {
    font-family: "Libre Caslon Text", serif;
    fill: var(--cream);
    letter-spacing: 1px;
  }
  .frame-message {
    font-family: "Alfa Slab One", serif;
    fill: var(--crimson-dark);
  }
  .banner-text {
    font-family: "Libre Caslon Text", serif;
    font-weight: 700;
    fill: var(--ink);
  }
  .phone {
    font-family: "Oswald", sans-serif;
    font-weight: 500;
    fill: var(--cream);
  }
</style>
</head>
<body>
<svg class="sign" viewBox="0 0 670 1000" xmlns="http://www.w3.org/2000/svg">
  <!-- shield body -->
  <path class="shield" fill="var(--sign-black)"
        d="M10,170 Q0,170 0,180 L0,770 Q30,780 30,810 L30,830 L335,990 L640,830 L640,810 Q640,780 665,770 L665,180 Q665,170 655,170 L470,165 Q460,18 335,3 Q210,18 200,165 Z"/>
  <path class="shield-trim" fill="none" stroke="var(--gold)" stroke-width="4"
        d="M22,190 L22,760 Q50,772 50,805 L50,820 L335,968 L620,820 L620,805 Q620,772 645,760 L645,190 L455,186 Q445,40 335,25 Q225,40 215,186 Z"/>

  <!-- medallion -->
  <circle class="medallion" cx="335" cy="150" r="122" fill="var(--gold)" stroke="var(--gold-deep)" stroke-width="4"/>

  <!-- corner ornaments -->
  <rect role="img" aria-label="Small gold filigree ornament" x="135" y="150" width="52" height="52" rx="8" fill="var(--gold-deep)"/>
  <rect role="img" aria-label="Small gold filigree ornament" x="483" y="150" width="52" height="52" rx="8" fill="var(--gold-deep)"/>

  <!-- business name -->
  <text class="sign-name" x="335" y="362" text-anchor="middle" font-size="104" textLength="600" lengthAdjust="spacingAndGlyphs">TALLPINE</text>

  <!-- divider arc -->
  <path d="M105,425 Q335,360 565,425" fill="none" stroke="var(--gold)" stroke-width="3"/>
  <path d="M335,372 l10,8 l-10,8 l-10,-8 Z" fill="var(--gold)"/>

  <text class="sign-subtitle" x="335" y="455" text-anchor="middle" font-size="34">FRAMING STUDIO</text>
  <line x1="105" y1="443" x2="150" y2="443" stroke="var(--gold)" stroke-width="2"/>
  <line x1="520" y1="443" x2="565" y2="443" stroke="var(--gold)" stroke-width="2"/>

  <!-- picture frame -->
  <rect class="frame-outer" x="55" y="472" width="555" height="292" fill="var(--gold)" stroke="var(--gold-deep)" stroke-width="4"/>
  <rect class="frame-moulding" x="82" y="498" width="501" height="240" fill="none" stroke="var(--gold-deep)" stroke-width="3"/>
  <rect class="frame-panel" x="115" y="525" width="435" height="195" fill="var(--gold-light)" stroke="var(--gold-deep)" stroke-width="3"/>

  <text class="frame-message" x="335" y="612" text-anchor="middle" font-size="80" textLength="300" lengthAdjust="spacingAndGlyphs">CUSTOM</text>
  <text class="frame-message" x="335" y="696" text-anchor="middle" font-size="80" textLength="350" lengthAdjust="spacingAndGlyphs">FRAMING</text>

  <!-- banner -->
  <path class="banner-tail" fill="var(--gold-deep)" d="M145,760 L70,815 L200,815 L200,785 Z"/>
  <path class="banner-tail" fill="var(--gold-deep)" d="M525,760 L600,815 L470,815 L470,785 Z"/>
  <path class="banner" fill="var(--gold)" stroke="var(--gold-deep)" stroke-width="2"
        d="M140,725 Q335,705 530,725 L525,790 Q335,775 145,795 Z"/>
  <text class="banner-text" x="335" y="762" text-anchor="middle" font-size="30">BY APPOINTMENT</text>

  <line x1="230" y1="800" x2="440" y2="800" stroke="var(--gold)" stroke-width="2"/>

  <!-- phone -->
  <text class="phone" x="335" y="882" text-anchor="middle" font-size="58">(555) 014-2276</text>

  <!-- bottom ornament -->
  <rect role="img" aria-label="Small gold scroll ornament" x="295" y="905" width="80" height="34" rx="10" fill="var(--gold-deep)"/>
</svg>
</body>
</html>
```